2020 K FILM FESTIVAL CAMPAIGN

Theme: 20/20 Vision
"For the 2020 Brambleton Film Festival, we are looking at the vision of the festival as well as filmmaking. We are asking Designers to recreate an Eye Chart Test. The first row/letter (typically 'E') will be where the Logo goes, the second row will have 20 20 pay attention to the spacing between the '20s, the third row will have the letters BFF again note the spacing. These first three lines ideally are creating a pyramid. We are looking for a funky grime kind of font for "BFF & 2020". Instead of letters, we want to use symbols and the chart gets smaller in text. We the following symbols should be the largest on the chart a "Black Power Fist" "Female Symbol" Transgender Symbol" "recycling symbol". All over symbols should relate to Film and Cinema and the fine arts.

Font styles to use
Sans Serif
Decorative

Colors

Designer to choose colors to be used in the design.

Requirements
Nice to have
• Fancy fonts

```html
<!DOCTYPE html>
<html lang="en">
<head>
<meta charset="utf-8">
<title>2020 K Film Festival – 20/20 Vision Eye Chart</title>
<link rel="stylesheet" href="https://fonts.googleapis.com/css2?family=Anton&family=Alfa+Slab+One&family=Arimo:wght@400;700&display=swap">
<style>
  :root {
    --backdrop: #2b2b2b;
    --paper: #ffffff;
    --ink: #111111;
    --vision-green: #34b34a;
    --reel-orange: #f07f22;
    --festival-gold: #e8a838;
  }
  * { box-sizing: border-box; margin: 0; padding: 0; }
  html, body { width: 1200px; height: 886px; overflow: hidden; }
  body { background: var(--backdrop); position: relative; font-family: "Arimo", Arial, sans-serif; color: var(--ink); }

  .poster { position: absolute; top: 67px; width: 531px; height: 750px; background: var(--paper); }
  .poster--chart { left: 54px; }
  .poster--clean { left: 615px; }

  .festival-name {
    position: absolute; left: calc(var(--cx) - 90px); top: calc(var(--cy) - 30px);
    width: 180px; height: 60px;
    display: flex; align-items: center; justify-content: center; gap: 8px;
  }
  .festival-name__dot {
    flex: none; width: var(--dot); height: var(--dot); border-radius: 50%;
    background: var(--festival-gold);
  }
  .festival-name__text {
    font-family: "Arimo", Arial, sans-serif; font-weight: 700; color: var(--ink);
    font-size: var(--fs); line-height: 1.15; letter-spacing: 0.5px;
  }

  .chart-row {
    position: absolute; left: var(--x); width: var(--w);
    top: calc(var(--cy) - var(--fs) * 0.6); height: calc(var(--fs) * 1.2);
    display: flex; justify-content: space-between; align-items: center;
    font-size: var(--fs); line-height: 1;
  }
  .chart-row--year { font-family: "Anton", Impact, sans-serif; }
  .chart-row--year span { display: inline-block; transform: scaleX(1.3); }
  .chart-row--year span:first-child { transform-origin: left center; }
  .chart-row--year span:last-child { transform-origin: right center; }
  .chart-row--letters { font-family: "Alfa Slab One", Georgia, serif; }
  .chart-row--icons { height: var(--fs); top: calc(var(--cy) - var(--fs) / 2); }
  .chart-row--icons svg { width: var(--fs); height: var(--fs); fill: var(--ink); }

  .band { position: absolute; left: var(--x); top: var(--y); width: var(--w); height: var(--h); }
  .band--green { background: var(--vision-green); }
  .band--orange { background: var(--reel-orange); }

  .acuity-scale { list-style: none; }
  .acuity-scale li {
    position: absolute; top: calc(var(--cy) - 10px); height: 20px; line-height: 20px;
    font-size: 16px; font-family: "Arimo", Arial, sans-serif;
  }
  .acuity-scale__line { left: 339px; width: 28px; text-align: center; }
  .acuity-scale__ratio { left: 394px; }
</style>
</head>
<body>

<svg width="0" height="0" style="position:absolute" aria-hidden="true">
  <symbol id="icon-eye" viewBox="0 0 24 24"><path d="M1 12 C5 5 19 5 23 12 C19 19 5 19 1 12Z M4 12 C7 16.5 17 16.5 20 12 C17 7.5 7 7.5 4 12Z"/><circle cx="12" cy="12" r="3.6"/></symbol>
  <symbol id="icon-camera" viewBox="0 0 24 24"><circle cx="7" cy="6" r="3.5"/><circle cx="15" cy="6" r="3.5"/><rect x="3" y="10" width="15" height="10" rx="1"/><path d="M18 13 L23 10 V20 L18 17Z"/></symbol>
  <symbol id="icon-masks" viewBox="0 0 24 24"><path d="M1 6 C5 4 9 4 12 6 C12 13 9 17 6.5 17 C4 17 1 13 1 6Z"/><path d="M11 9 C15 7 19 7 23 9 C23 16 20 20 17 20 C14 20 11 16 11 9Z"/></symbol>
  <symbol id="icon-popcorn" viewBox="0 0 24 24"><path d="M5 6 C5 2 9 2 10 3.5 C11 1.5 14 1.5 15 3.5 C16 2 19 2.5 19 6Z"/><path d="M5 8 H19 L17 23 H7Z M9 9 L9.8 22 H10.8 L10 9Z M14 9 L13.2 22 H14.2 L15 9Z" fill-rule="evenodd"/></symbol>
  <symbol id="icon-clapper" viewBox="0 0 24 24"><path d="M2 4 L20 1 L21 5 L3 8Z"/><rect x="3" y="10" width="18" height="12"/></symbol>
  <symbol id="icon-ticket" viewBox="0 0 24 24"><path d="M14 2 L22 10 L19 13 C18 12 16.5 12 15.8 12.8 C15 13.5 15 15 16 16 L10 22 L2 14 L8 8 C9 9 10.5 9 11.2 8.2 C12 7.5 12 6 11 5Z"/></symbol>
  <symbol id="icon-badge" viewBox="0 0 24 24"><circle cx="12" cy="12" r="10" fill="none" stroke="#111" stroke-width="2"/></symbol>
</svg>

<section class="poster poster--chart">
  <div class="festival-name" style="--cx:183px; --cy:149px; --fs:14px; --dot:22px;">
    <span class="festival-name__dot"></span>
    <span class="festival-name__text">BRAMBLETON<br>FILM FESTIVAL</span>
  </div>

  <div class="chart-row chart-row--year" style="--x:102px; --w:157px; --cy:255px; --fs:57px;"><span>20</span><span>20</span></div>
  <div class="chart-row chart-row--letters" style="--x:101px; --w:166px; --cy:327px; --fs:56px;"><span>B</span><span>F</span><span>F</span></div>
  <div class="chart-row chart-row--letters" style="--x:101px; --w:169px; --cy:383px; --fs:35px;"><span>F</span><span>C</span><span>V</span><span>Z</span></div>
  <div class="chart-row chart-row--letters" style="--x:101px; --w:172px; --cy:426px; --fs:30px;"><span>I</span><span>M</span><span>G</span><span>N</span><span>R</span></div>
  <div class="chart-row chart-row--letters" style="--x:101px; --w:171px; --cy:460px; --fs:24px;"><span>B</span><span>R</span><span>A</span><span>M</span><span>B</span><span>L</span></div>
  <div class="band band--green" style="--x:92px; --y:476px; --w:185px; --h:13px;"></div>
  <div class="chart-row chart-row--icons" style="--x:112px; --w:146px; --cy:512px; --fs:14px;">
    <svg><use href="#icon-eye"/></svg><svg><use href="#icon-camera"/></svg><svg><use href="#icon-masks"/></svg><svg><use href="#icon-popcorn"/></svg><svg><use href="#icon-clapper"/></svg><svg><use href="#icon-ticket"/></svg><svg><use href="#icon-badge"/></svg>
  </div>
  <div class="chart-row chart-row--letters" style="--x:114px; --w:145px; --cy:549px; --fs:15px;"><span>F</span><span>I</span><span>L</span><span>M</span><span>F</span><span>E</span><span>S</span><span>T</span></div>
  <div class="band band--orange" style="--x:112px; --y:562px; --w:148px; --h:13px;"></div>
  <div class="chart-row chart-row--letters" style="--x:111px; --w:151px; --cy:596px; --fs:9px;"><span>D</span><span>A</span><span>T</span><span>E</span><span>2</span><span>7</span><span>T</span><span>H</span></div>
  <div class="chart-row chart-row--letters" style="--x:125px; --w:124px; --cy:627px; --fs:9px;"><span>A</span><span>P</span><span>R</span><span>I</span><span>L</span><span>5</span><span>T</span><span>H</span></div>
  <div class="chart-row chart-row--letters" style="--x:155px; --w:51px; --cy:658px; --fs:9px;"><span>2</span><span>0</span><span>2</span><span>0</span></div>

  <ul class="acuity-scale">
    <li class="acuity-scale__line" style="--cy:150px">1</li><li class="acuity-scale__ratio" style="--cy:150px">20/200</li>
    <li class="acuity-scale__line" style="--cy:255px">2</li><li class="acuity-scale__ratio" style="--cy:255px">20/100</li>
    <li class="acuity-scale__line" style="--cy:328px">3</li><li class="acuity-scale__ratio" style="--cy:328px">20/70</li>
    <li class="acuity-scale__line" style="--cy:383px">4</li><li class="acuity-scale__ratio" style="--cy:383px">20/50</li>
    <li class="acuity-scale__line" style="--cy:426px">5</li><li class="acuity-scale__ratio" style="--cy:426px">20/40</li>
    <li class="acuity-scale__line" style="--cy:460px">6</li><li class="acuity-scale__ratio" style="--cy:460px">20/30</li>
    <li class="acuity-scale__line" style="--cy:512px">7</li><li class="acuity-scale__ratio" style="--cy:512px">20/25</li>
    <li class="acuity-scale__line" style="--cy:550px">8</li><li class="acuity-scale__ratio" style="--cy:550px">20/20</li>
    <li class="acuity-scale__line" style="--cy:596px">9</li>
    <li class="acuity-scale__line" style="--cy:627px">10</li>
    <li class="acuity-scale__line" style="--cy:658px">11</li>
  </ul>
</section>

<section class="poster poster--clean">
  <div class="festival-name" style="--cx:265px; --cy:104px; --fs:16px; --dot:26px;">
    <span class="festival-name__dot"></span>
    <span class="festival-name__text">BRAMBLETON<br>FILM FESTIVAL</span>
  </div>

  <div class="chart-row chart-row--year" style="--x:173px; --w:187px; --cy:231px; --fs:66px;"><span>20</span><span>20</span></div>
  <div class="chart-row chart-row--letters" style="--x:167px; --w:200px; --cy:317px; --fs:61px;"><span>B</span><span>F</span><span>F</span></div>
  <div class="chart-row chart-row--letters" style="--x:165px; --w:202px; --cy:383px; --fs:43px;"><span>F</span><span>C</span><span>V</span><span>Z</span></div>
  <div class="chart-row chart-row--letters" style="--x:163px; --w:206px; --cy:436px; --fs:34px;"><span>I</span><span>M</span><span>G</span><span>N</span><span>R</span></div>
  <div class="chart-row chart-row--letters" style="--x:165px; --w:204px; --cy:476px; --fs:25px;"><span>B</span><span>R</span><span>A</span><span>M</span><span>B</span><span>L</span></div>
  <div class="band band--green" style="--x:155px; --y:495px; --w:221px; --h:16px;"></div>
  <div class="chart-row chart-row--icons" style="--x:179px; --w:174px; --cy:537px; --fs:17px;">
    <svg><use href="#icon-eye"/></svg><svg><use href="#icon-camera"/></svg><svg><use href="#icon-masks"/></svg><svg><use href="#icon-popcorn"/></svg><svg><use href="#icon-clapper"/></svg><svg><use href="#icon-ticket"/></svg><svg><use href="#icon-badge"/></svg>
  </div>
  <div class="chart-row chart-row--letters" style="--x:180px; --w:172px; --cy:582px; --fs:16px;"><span>F</span><span>I</span><span>L</span><span>M</span><span>F</span><span>E</span><span>S</span><span>T</span></div>
  <div class="band band--orange" style="--x:177px; --y:597px; --w:177px; --h:16px;"></div>
  <div class="chart-row chart-row--letters" style="--x:176px; --w:181px; --cy:638px; --fs:12px;"><span>D</span><span>A</span><span>T</span><span>E</span><span>2</span><span>7</span><span>T</span><span>H</span></div>
  <div class="chart-row chart-row--letters" style="--x:192px; --w:147px; --cy:675px; --fs:11px;"><span>A</span><span>P</span><span>R</span><span>I</span><span>L</span><span>5</span><span>T</span><span>H</span></div>
  <div class="chart-row chart-row--letters" style="--x:236px; --w:60px; --cy:712px; --fs:11px;"><span>2</span><span>0</span><span>2</span><span>0</span></div>
</section>

</body>
</html>
```